Somebody commencing retirement at age 67 and wanting a card to introduce myself

Something that depicts the activities I intend to pursue in retirement: Travel, Golf (both in Australia and internationally), wining (red) and dining and generally leading a decadent lifestyle with my wife (or by myself as appropriate).

I offer no services, but intend to have a decadent, relaxing
retirement, playing golf, drinking red wine and dining at good
restaurants!

The card needs to have a suitably designed logo that reflects the
foregoing.

Requirements
Must have
• On the front of the card, my photograph (attached and cropped as
• appropriate), my name (Carl Brimstead), my mobile phone number (+61 417
• 532 148), my email address (carl@brimstead.example.au) and my residential
• address (41 Kestrel Lane, Marlowe Heights, Western Australia 6031,
• Australia).
• The rear of the card should have my postal address (Carl Brimstead
• Post Office Box 518 Dunmore Western Australia 6947, Australia.)._

```html
<!DOCTYPE html>
<html lang="en">
<head>
<meta charset="utf-8">
<title>Carl Brimstead – Retirement Card</title>
<link href="https://fonts.googleapis.com/css2?family=Roboto+Condensed:wght@400;700&display=swap" rel="stylesheet">
<style>
  :root {
    --backdrop: #bcbdc0;
    --card: #ffffff;
    --panel: #e6e6e6;
    --frame: #c9c9c9;
    --text: #7a7a7c;
    --accent: #c0185a;
    --photo-light: #e7e2da;
    --photo-mid: #b9a58f;
    --photo-dark: #5d6b45;
  }
  * { margin: 0; padding: 0; box-sizing: border-box; }
  html, body { width: 1200px; height: 1200px; overflow: hidden; }
  body {
    position: relative;
    background: var(--backdrop);
    font-family: "Roboto Condensed", "Arial Narrow", sans-serif;
    color: var(--text);
  }
  .card {
    position: absolute;
    left: 230px;
    width: 732px;
    height: 405px;
    background: var(--card);
    border-radius: 24px;
    overflow: hidden;
  }
  .card--front { top: 148px; }
  .card--back { top: 645px; }

  .front-diagonal { position: absolute; inset: 0; }

  .brand {
    position: absolute;
    left: 40px;
    top: 39px;
    width: 251px;
    height: 109px;
    display: flex;
    align-items: center;
    gap: 16px;
  }
  .brand__square { width: 46px; height: 46px; background: var(--accent); }
  .brand__name { font-size: 34px; font-weight: 700; color: var(--text); }

  .holder-name {
    position: absolute;
    left: 38px;
    top: 194px;
    font-size: 35px;
    font-weight: 700;
    letter-spacing: -0.2px;
  }
  .contact {
    position: absolute;
    left: 38px;
    top: 250px;
    font-size: 21px;
    line-height: 29.5px;
    white-space: nowrap;
  }
  .contact strong { font-weight: 700; }

  .portrait-frame {
    position: absolute;
    left: 488px;
    top: 40px;
    width: 205px;
    height: 329px;
    border: 2px solid var(--frame);
    background: #f4f4f4;
    padding: 7px;
  }
  .portrait {
    width: 100%;
    height: 100%;
    background: linear-gradient(160deg, var(--photo-dark) 0%, var(--photo-mid) 40%, var(--photo-light) 75%, #f3ebe6 100%);
  }

  .back-panel {
    position: absolute;
    left: 40px;
    top: 40px;
    width: 651px;
    height: 324px;
    background: var(--panel);
    border-radius: 18px;
    text-align: center;
  }
  .back-panel__name {
    margin-top: 122px;
    font-size: 27px;
    font-weight: 700;
  }
  .back-panel__address {
    font-size: 21px;
    margin-top: 2px;
  }
</style>
</head>
<body>
  <section class="card card--front">
    <svg class="front-diagonal" width="732" height="405" viewBox="0 0 732 405" aria-hidden="true">
      <polygon points="310,405 700,0 732,0 732,405" fill="var(--panel)"/>
    </svg>

    <div class="brand">
      <span class="brand__square"></span>
      <span class="brand__name">Brimstead</span>
    </div>

    <h1 class="holder-name">Carl Brimstead</h1>
    <p class="contact">
      <strong>Phone.</strong> +61 417 532 148<br>
      <strong>Email.</strong> carl@brimstead.example.au<br>
      <strong>Residential address.</strong> 41 Kestrel Lane<br>
      Marlowe Heights, Western Australia 6031, Australia
    </p>

    <div class="portrait-frame">
      <div class="portrait" role="img" aria-label="Portrait photograph of the cardholder and his wife, smiling outdoors"></div>
    </div>
  </section>

  <section class="card card--back">
    <div class="back-panel">
      <p class="back-panel__name">Carl Brimstead</p>
      <p class="back-panel__address">Post Office Box 518 Dunmore Western Australia 6947, Australia.</p>
    </div>
  </section>
</body>
</html>
```